Real Estate Agent Service Brochure

I need a trifold brochure to showcase my real estate services. I am a veteran Real Estate Broker specializing in marketing properties for sale and for top dollar. I would like to see designs that use colors from my logo (attached) and I would like to showcase some before and after photos of staging jobs I have done to homes to get them ready for the market. This brochure is specific to home sellers. You are happy to go check out my website for inspiration www.lomavertpa.com but keep the copy as I have written it. The the final design should communicate experienced professional who uses current technologies and strategies to market properties for the highest value.

Target Market(s)

Homeowners wanting to sell their homes

Industry/Entity Type

Real Estate Agent

Font styles to use
Serif

Requirements
Must have
• My, logo, personal photo, title and contact information as listed:
• Marta Venholt
• Owner Broker
• Stager Re-Designer
• 860-912-7048
• BRAVE Realty LLC
• LOMAVERTPA.com
• Marta@LOMAVERTPA.com
• The colors used should be those in my logo.
• Brochure should be able to fit in standard envelope for mailing.
Nice to have
• I think I would like my personal photo and contact information on the front panel.
Should not have
• Bright colors.

```html
<!DOCTYPE html>
<html lang="en">
<head>
<meta charset="utf-8">
<title>BRAVE Realty LLC – Seller Brochure</title>
<link rel="stylesheet" href="https://fonts.googleapis.com/css2?family=Open+Sans:wght@400;600&display=swap">
<style>
  :root{
    --band:#545456;
    --band-dark:#4a4a4c;
    --navy:#1b2a52;
    --ink:#3c3c3e;
    --paper:#f3f3f3;
    --white:#ffffff;
  }
  *{box-sizing:border-box;margin:0;padding:0}
  html,body{width:1200px;height:936px;overflow:hidden;background:#d6d6d8}
  body{font-family:"Open Sans",Arial,sans-serif;color:var(--ink)}
  .brochure{position:relative;width:1200px;height:936px;background:var(--paper);overflow:hidden}
  .abs{position:absolute}

  .top-band{left:0;top:0;width:1200px;height:158px;background:var(--band)}
  .top-band-left{left:0;top:0;width:391px;height:158px;background:var(--band-dark)}
  .bottom-band{left:0;top:895px;width:1200px;height:41px;background:var(--band)}
  .bottom-band-left{left:0;top:895px;width:391px;height:41px;background:var(--band-dark)}

  .cover-heading{left:22px;top:46px;color:var(--white);font-size:26px;line-height:38px;font-weight:400;letter-spacing:.3px}
  .top-url{left:503px;top:78px;color:var(--white);font-size:16px;letter-spacing:.4px}
  .brand-top{left:880px;top:62px;width:300px;color:var(--white);font-size:28px;font-weight:600;letter-spacing:.5px;text-align:center;white-space:nowrap}

  .intro-panel{left:0;top:158px;width:391px;height:406px;background:linear-gradient(90deg,#ffffff,#f0f0f0)}
  .intro-copy{left:22px;top:196px;width:351px;font-size:15px;line-height:23.5px;color:#4a4a4c}
  .intro-copy p{margin-bottom:23px;text-align:justify}
  .intro-copy p:first-child{text-align:left}
  .intro-copy .wrap-short{display:block;width:230px;text-align:left}
  .agent-name{left:22px;top:486px;color:var(--navy);font-size:20px;white-space:nowrap}
  .agent-title{left:22px;top:515px;color:var(--navy);font-size:16px;line-height:21px;font-weight:600;white-space:nowrap}

  .photo-house{left:0;top:564px;width:391px;height:331px;background:linear-gradient(160deg,#8c7a62,#5a4a36 55%,#3e3a2a)}
  .photo-agent-head{left:262px;top:396px;width:190px;height:200px;border-radius:95px 95px 40px 40px;background:linear-gradient(180deg,#a9a39d 0%,#8f857c 70%,#6e655e 100%)}
  .photo-agent-body{left:140px;top:580px;width:335px;height:315px;border-radius:90px 90px 0 0;background:linear-gradient(180deg,#2a2a2c 0%,#1a1a1c 40%,#141416 100%)}
  .photo-room{left:391px;top:158px;width:809px;height:488px;background:linear-gradient(180deg,#e9e6e0 0%,#dcd6cc 55%,#6b5a4c 82%,#4a3a30 100%)}

  .contact-panel{left:475px;top:646px;width:337px;height:249px;background:linear-gradient(90deg,#ffffff,#ececec)}
  .brand-main{left:497px;top:694px;color:var(--navy);font-size:29px;font-weight:600;letter-spacing:.5px;white-space:nowrap}
  .contact-list{left:497px;top:802px;list-style:none;color:var(--navy);font-size:16px}
  .contact-list li{display:flex;align-items:center;height:29px;white-space:nowrap}
  .contact-list svg{width:20px;height:20px;margin-right:9px;flex:none}

  .feature-box{left:812px;top:578px;width:388px;height:137px;background:var(--navy)}
  .feature-heading{right:44px;top:18px;color:var(--white);font-size:32px;line-height:48px;text-align:right;font-weight:400;white-space:nowrap}
  .seller-panel{left:812px;top:715px;width:388px;height:180px;background:linear-gradient(90deg,#ececec,#f7f7f7)}
  .seller-copy{right:22px;top:28px;width:330px;text-align:right;font-size:15.5px;line-height:19.5px;color:#4a4a4c}
  .seller-url{right:22px;top:151px;color:var(--navy);font-size:16px}
</style>
</head>
<body>
<main class="brochure">
  <div class="abs top-band"></div>
  <div class="abs top-band-left"></div>
  <h1 class="abs cover-heading">PROVEN MARKET<br>KNOWLEDGE</h1>
  <div class="abs top-url">www.lomavertpa.com</div>
  <div class="abs brand-top">BRAVE Realty LLC</div>

  <section class="abs intro-panel"></section>
  <div class="abs intro-copy">
    <p>That’s what you can expect when you work with seasoned specialist Marta Venholt for all your Real Estate needs.</p>
    <p>The sale of a home is too important an undertaking to entrust to just anyone. Select a dedicated, service-oriented and results-driven broker who understands the <span class="wrap-short">intricacies of the Real Estate process...<br>select Marta Venholt.</span></p>
  </div>
  <div class="abs agent-name">Marta Venholt</div>
  <div class="abs agent-title">Owner Broker<br>Stage Re-Designer</div>

  <div class="abs photo-room" role="img" aria-label="Staged living room with white sofas, fireplace and built-in shelves"></div>
  <div class="abs photo-house" role="img" aria-label="Wooden house among autumn trees"></div>

  <section class="abs contact-panel"></section>
  <div class="abs photo-agent-body" role="img" aria-label="Portrait of the broker in a dark blazer, arms crossed"></div>
  <div class="abs photo-agent-head" aria-hidden="true"></div>

  <div class="abs brand-main">BRAVE Realty LLC</div>
  <ul class="abs contact-list">
    <li><svg viewBox="0 0 20 20"><circle cx="10" cy="10" r="9" fill="none" stroke="var(--navy)" stroke-width="2"/><path d="M7 5.5l2 2-1 1.5c.6 1.3 1.7 2.4 3 3l1.5-1 2 2-1.3 1.5c-3.3-.5-6.2-3.4-6.7-6.7z" fill="var(--navy)"/></svg>860-912-7048</li>
    <li><svg viewBox="0 0 20 20"><circle cx="10" cy="10" r="9" fill="none" stroke="var(--navy)" stroke-width="2"/><rect x="5.5" y="7" width="9" height="6.5" fill="none" stroke="var(--navy)" stroke-width="1.5"/><path d="M5.5 7l4.5 3.5 4.5-3.5" fill="none" stroke="var(--navy)" stroke-width="1.5"/></svg>Marta@LOMAVERTPA.com</li>
    <li><svg viewBox="0 0 20 20"><circle cx="10" cy="10" r="9" fill="none" stroke="var(--navy)" stroke-width="2"/><circle cx="10" cy="10" r="5.5" fill="none" stroke="var(--navy)" stroke-width="1.3"/><path d="M4.5 10h11M10 4.5c-2.5 3-2.5 8 0 11M10 4.5c2.5 3 2.5 8 0 11" fill="none" stroke="var(--navy)" stroke-width="1.2"/></svg>www.LOMAVERTPA.com</li>
  </ul>

  <section class="abs feature-box">
    <h2 class="abs feature-heading">PROVEN MARKET<br>KNOWLEDGE</h2>
  </section>
  <section class="abs seller-panel">
    <p class="abs seller-copy">Having the right marketing partner is so important; one who works to protect your best interests while capably navigating you through the many complexities of the real estate transaction is vital.</p>
    <div class="abs seller-url">www.LOMAVERTPA.com</div>
  </section>

  <div class="abs bottom-band"></div>
  <div class="abs bottom-band-left"></div>
</main>
</body>
</html>
```